Web Design Project for Sports Bar

We are redesigning a new clients webpage. Old site is VERY antiquated. The client is a sports bar in the Seattle Area.

Bar's name: The Copper Lantern

This sports bar has pool tables, darts, poker, dancing with a DJ every Wed-Saturday.
They have area for watching major sporting events. KTB, PWJ, QDR, VGT, JXP, etc...

Every holiday they typically host events for their patrons.

This could be a combo job. They have 2 bar's with slightly different genre. We are redesigning both sites.

We want to have Trelvio plugin integrated and other social media references, (i.e. Quib)

We have guaranteed the funds for this site.  We also have another that is similar that we will be posting again for a sister bar.  This could be a 2 for one deal.  Our client is anxiously looking for some examples.  Please post your designs if you are close.  

Reason: client was out of town is now just reviewing designs. hopefully will have some meaningful feedback soon.

Target Market(s)

Age 21-50, Sports enthusiasts, dancers, "hiphopsters"

Industry/Entity Type

Sports Bar

Requirements
Must have
• Navigation will be:

Home
Menus
Events
KTB
PWJ
Poker
Entertainment
Karaoke
DJ Dancing
Group Parties
Location/Directions
Contact

```html
<!DOCTYPE html>
<html lang="en">
<head>
<meta charset="utf-8">
<title>The Copper Lantern – Sports Bar</title>
<link href="https://fonts.googleapis.com/css2?family=Open+Sans:wght@400;600;700;800&display=swap" rel="stylesheet">
<style>
:root{
  --orange:#f7901e;
  --orange-light:#ffb43c;
  --orange-dark:#e06a0a;
  --ink:#000;
  --panel:#141414;
  --field:#3d3d3d;
  --text-muted:#9a9a9a;
  --white:#fff;
  --map-base:#e9e7e1;
  --map-road:#f3d27a;
  --pin:#c8404a;
}
*{box-sizing:border-box;margin:0;padding:0}
html,body{width:886px;height:1200px;overflow:hidden;background:var(--ink)}
body{font-family:"Open Sans",Arial,sans-serif;color:var(--white)}
a{text-decoration:none;color:inherit}
.page{position:relative;width:886px;height:1200px;overflow:hidden;
  background:
   radial-gradient(ellipse 260px 180px at 40px 250px,rgba(255,140,30,.55),transparent 70%),
   radial-gradient(ellipse 260px 200px at 860px 260px,rgba(255,130,20,.5),transparent 70%),
   radial-gradient(ellipse 500px 260px at 440px 60px,rgba(255,150,40,.55),transparent 75%),
   linear-gradient(180deg,#8a3a08 0%,#c2560e 12%,#7a2c06 28%,#2a0c02 42%,#000 52%);}
.phone{position:absolute;left:623px;top:0;width:169px;height:28px;background:#2a1e16;
  display:flex;align-items:center;justify-content:center;gap:7px;font-weight:700;font-size:18px}
.brand{position:absolute;left:91px;top:24px;font-weight:800;font-size:42px;letter-spacing:-.5px;
  color:#ececec;white-space:nowrap}
.social{position:absolute;left:620px;top:41px;display:flex;gap:4px}
.social a{display:flex;flex-direction:column;align-items:center;justify-content:center;gap:3px;width:40px;height:38px;
  font-size:7.5px;font-weight:600;color:var(--white);background:#1c1c1c;border-radius:4px}
.social i{width:10px;height:10px;background:var(--orange);display:block}
.nav{position:absolute;left:89px;top:87px;width:703px;height:36px;display:flex;
  background:linear-gradient(#333,#0c0c0c);border:1px solid #000}
.nav a{display:flex;align-items:center;justify-content:center;color:var(--white);
  font-weight:600;font-size:17px;border-right:1px solid #000;box-shadow:1px 0 0 #3a3a3a}
.nav a:last-child{border-right:0;box-shadow:none}
.nav a.active{background:linear-gradient(#181818,#000)}
.slider{position:absolute;left:90px;top:136px;width:702px;height:324px;background:#161616;border:1px solid #2c2c2c}
.arrow{position:absolute;top:268px}
.event{position:absolute;top:18px;width:218px;height:288px;overflow:hidden}
.event-art{position:absolute;inset:0}
.date{position:absolute;left:8px;top:2px;font-weight:800;font-size:66px;letter-spacing:-3px;line-height:1;
  color:var(--white);-webkit-text-stroke:1.5px #000}
.day{position:absolute;left:16px;top:66px;width:104px;height:27px;background:var(--orange);
  font-size:18px;padding-left:9px;line-height:27px}
.event-bar{position:absolute;left:0;right:0;top:196px;height:50px;background:rgba(0,0,0,.6);
  color:var(--orange);font-weight:600;font-size:32px;text-align:center;line-height:48px;white-space:nowrap}
.pill{display:inline-block;border-radius:14px;background:linear-gradient(var(--orange-light),var(--orange-dark));
  color:var(--white);font-weight:600;font-size:14px;text-align:center;border:1px solid #ffd08a;text-shadow:0 1px 1px rgba(0,0,0,.4)}
.event .pill{position:absolute;left:69px;top:250px;width:82px;height:22px;line-height:20px}
.content{position:absolute;left:90px;top:484px;width:700px;height:484px;background:var(--panel)}
h2{position:absolute;font-weight:600;font-size:32px;letter-spacing:1px;line-height:1}
.map{position:absolute;left:15px;top:51px;width:240px;height:257px;
  background:linear-gradient(125deg,var(--map-base) 0%,#dcdad3 45%,#ebe6cf 100%);border:1px solid #888}
.map svg{position:absolute;left:141px;top:137px}
.field{position:absolute;left:276px;width:202px;height:32px;background:var(--field);border-radius:3px;
  font-size:13px;padding:7px 11px;color:#eee;box-shadow:inset 0 0 0 1px #4a4a4a}
.field svg{position:absolute;right:8px;top:7px}
.field.message{height:113px}
.send{position:absolute;left:276px;top:274px;width:202px;height:34px;border-radius:3px;
  background:linear-gradient(var(--orange-light),var(--orange-dark));font-size:17px;text-align:center;line-height:34px;font-weight:600}
.social-box{position:absolute;left:503px;top:51px;width:176px;height:242px;background:var(--white);border:1px solid #bbb;color:#333;padding:8px 7px;font-family:Arial,sans-serif}
.social-box .title{display:flex;gap:6px;font-size:11px;font-weight:700;color:#3b5998;line-height:1.15}
.social-box .mark{width:26px;height:22px;background:var(--orange);flex:none}
.like{display:inline-block;margin:6px 0 0 6px;border:1px solid #bbb;background:#f2f2f2;font-size:9px;padding:2px 5px;color:#333}
.fans-note{font-size:8px;margin:10px 0 6px;line-height:1.3}
.fans{display:grid;grid-template-columns:repeat(4,36px);gap:4px 7px}
.fans div{font-size:7px;text-align:center;color:#777;white-space:nowrap}
.fans span{display:block;width:36px;height:38px;background:linear-gradient(#b59a86,#6b5648);margin-bottom:2px}
.plug{position:absolute;left:7px;right:7px;bottom:4px;border-top:1px solid #ccc;font-size:7px;color:#3b5998;padding-top:3px}
.welcome p{position:absolute;left:21px;top:357px;width:670px;font-size:12px;line-height:16px;color:var(--text-muted)}
.read{position:absolute;left:21px;top:444px;width:83px;height:24px;line-height:22px}
.sponsors-title{left:92px;top:980px}
.sponsors{position:absolute;left:92px;top:1029px;width:700px;height:88px}
.footer{position:absolute;left:0;top:1136px;width:886px;height:64px;background:#161616;border-top:1px solid #2e2e2e;text-align:center}
.footer p{font-size:13px;margin-top:14px}
.footer small{display:block;font-size:10px;color:#555;margin-top:2px}
</style>
</head>
<body>
<div class="page">
  <div class="phone">
    <svg width="16" height="16" viewBox="0 0 16 16"><path d="M4 1l2 3-1.5 1.5c.8 2 2.5 3.7 4.5 4.5L10.5 8.5l3 2-1.2 2.8C7 13 3 9 2.7 3.7z" fill="#fff"/></svg>
    0900-555-01
  </div>
  <div class="brand">The Copper Lantern</div>
  <div class="social">
    <a href="#"><i></i>Trelvio</a>
    <a href="#"><i></i>Chirpline</a>
    <a href="#"><i></i>Plusora</a>
    <a href="#"><i></i>Vidnook</a>
  </div>

  <nav class="nav">
    <a class="active" href="#" style="width:121px">Home</a>
    <a href="#" style="width:112px">Menus</a>
    <a href="#" style="width:108px">Events</a>
    <a href="#" style="width:216px">Location/Directions</a>
    <a href="#" style="width:146px">Contact</a>
  </nav>

  <svg class="arrow" style="left:48px" width="34" height="46" viewBox="0 0 34 46"><path d="M26 3L8 23l18 20" fill="none" stroke="#eee" stroke-width="8"/></svg>
  <svg class="arrow" style="left:804px" width="34" height="46" viewBox="0 0 34 46"><path d="M8 3l18 20L8 43" fill="none" stroke="#eee" stroke-width="8"/></svg>

  <section class="slider">
    <article class="event" style="left:13px">
      <div class="event-art" role="img" aria-label="Poster photo of two fighters for the PWJ live broadcast" style="background:linear-gradient(160deg,#5a4034,#3a2a22 45%,#1c1410 70%,#4a1010)"></div>
      <div class="date">02.04</div><div class="day">Tueday</div>
      <div class="event-bar">PWJ Live</div>
      <a class="pill" href="#">More Info</a>
    </article>
    <article class="event" style="left:243px">
      <div class="event-art" role="img" aria-label="Photo of a crowd dancing at a party" style="background:linear-gradient(160deg,#c87a40,#8a3a2a 40%,#3a3a5a 75%,#7a7a9a)"></div>
      <div class="date">02.04</div><div class="day">Tueday</div>
      <div class="event-bar">Dance Party</div>
      <a class="pill" href="#">More Info</a>
    </article>
    <article class="event" style="left:473px">
      <div class="event-art" role="img" aria-label="Photo of a band playing a live gig" style="background:linear-gradient(160deg,#d8a8e0,#9a4ab0 40%,#5a2a7a 70%,#c060c0)"></div>
      <div class="date">02.04</div><div class="day">Tueday</div>
      <div class="event-bar">Live GIG</div>
      <a class="pill" href="#">More Info</a>
    </article>
  </section>

  <section class="content">
    <h2 style="left:17px;top:9px">Find Us :</h2>
    <div class="map" role="img" aria-label="Street map showing the bar's location">
      <svg width="34" height="50" viewBox="0 0 34 50"><path d="M17 1C8 1 1 8 1 17c0 11 16 32 16 32s16-21 16-32C33 8 26 1 17 1z" fill="var(--pin)"/><circle cx="17" cy="17" r="6" fill="#e8a0a6"/></svg>
    </div>

    <h2 style="left:288px;top:9px">Contact us</h2>
    <div class="field" style="top:53px">Your Name
      <svg width="18" height="18" viewBox="0 0 18 18"><circle cx="9" cy="5" r="4" fill="var(--orange)"/><path d="M1 18c0-5 4-7 8-7s8 2 8 7z" fill="var(--orange)"/></svg></div>
    <div class="field" style="top:97px">Your Email
      <svg width="22" height="16" viewBox="0 0 22 16"><rect x="1" y="2" width="20" height="13" fill="var(--orange)"/><path d="M1 2l10 8 10-8" fill="none" stroke="#3d3d3d" stroke-width="1.5"/></svg></div>
    <div class="field message" style="top:141px">Your Message
      <svg width="22" height="20" viewBox="0 0 22 20"><ellipse cx="11" cy="8" rx="10" ry="7.5" fill="var(--orange)"/><path d="M5 13l-2 6 7-4z" fill="var(--orange)"/></svg></div>
    <div class="send">Shoot It</div>

    <aside class="social-box">
      <div class="title"><span class="mark"></span><span>Rankwell Co - Search Listing Services <small style="font-weight:400">on Trelvio</small></span></div>
      <span class="like">Like</span>
      <p class="fans-note">1,490 people like <b>Rankwell Co - Search Listing Services.</b></p>
      <div class="fans" role="img" aria-label="Profile photos of followers">
        <div><span></span>Mara</div><div><span></span>Jo</div><div><span></span>Henri Dale</div><div><span></span>Kent</div>
        <div><span></span>Sal</div><div><span></span>Tavin</div><div><span></span>Rex</div><div><span></span>Dana</div>
      </div>
      <div class="plug">Trelvio social plugin</div>
    </aside>

    <div class="welcome">
      <h2 style="left:21px;top:321px">Welcome</h2>
      <p>Lorem ipsum dolor sit amet, consectetur adipiscing elit. Etiam vitae urna eu felis mtollis hendrerit non nec mi. Pellentesque nec velit non velit tincidunt lobortis ac sed elit. Donec sed velit nulla, vel elementum mi. Aliquam erat volutpat. Curabitur aliquam nisl sit amet ipsum venenatis eget tincidunt metus pellentesque. Aliquam eleifend eros quis purus hendrerit rutrum. Lorem ipsum dolor sit amet, consectetur adipiscing elit. Etiam vitae urna eu felis mollis hendrerit non nec mi.</p>
      <a class="pill read" href="#">Read More</a>
    </div>
  </section>

  <h2 class="sponsors-title">Sponsors :</h2>
  <svg class="sponsors" viewBox="0 0 700 88" role="img" aria-label="Neon signs of the bar's sponsors">
    <circle cx="46" cy="44" r="41" fill="#1f7a2a" stroke="#111" stroke-width="3"/>
    <ellipse cx="170" cy="44" rx="60" ry="36" fill="#1a0820" stroke="#e060ff" stroke-width="3"/>
    <ellipse cx="322" cy="44" rx="62" ry="38" fill="#0a1620" stroke="#60d8ff" stroke-width="3"/>
    <ellipse cx="478" cy="44" rx="60" ry="36" fill="#1a1400" stroke="#ffd020" stroke-width="4"/>
    <ellipse cx="633" cy="44" rx="56" ry="34" fill="#0c0c18" stroke="#8aa0ff" stroke-width="3"/>
  </svg>

  <footer class="footer">
    <p>Copyright 2012 - Copper Lantern</p>
    <small>Terms &amp; Conditions &nbsp;|&nbsp; Privacy Policy</small>
  </footer>
</div>
</body>
</html>
```